Pebble and Pine App design

I need a full app design, colours, images, fonts, and a mock up design of the app to bring to the developer.

Pebble and Pine is a free app that allows cafes, independent cafe and chains of cafes to let their customers know what the soup of the day and what specials they have on that day through the app. Each cafe will have a profile which they can upload the Pebble and Pine daily.

The user home screen will include google maps showing their location with the registered cafes and eateries around them. including a list of the cafe and distances below. as seen in attachment.

Target Market(s)

Cafes , anyone who enjoys eating soups and off local cafe specials boards

Requirements
Must have
• I would like a complete app design based on the attached images.

```html
<!DOCTYPE html>
<html lang="en">
<head>
<meta charset="utf-8">
<title>Pebble and Pine – App Design</title>
<link rel="stylesheet" href="https://fonts.googleapis.com/css2?family=Arimo:wght@400;700&family=Nunito:wght@400;600;700;800&display=swap">
<style>
  :root {
    --brand-red: #e85757;
    --cocoa: #7d5a57;
    --white: #ffffff;
    --ink: #2f2f2f;
    --rule: #d9d9d9;
    --map-light: #f0eeea;
    --map-warm: #f6ecdd;
    --map-green: #cfe6c0;
  }
  * { box-sizing: border-box; margin: 0; padding: 0; }
  html, body { width: 1200px; height: 1200px; overflow: hidden; }
  body { background: var(--brand-red); position: relative; font-family: "Nunito", sans-serif; }

  .intro { position: absolute; left: 112px; top: 372px; width: 390px; color: var(--white); font-family: "Arimo", sans-serif; }
  .intro-title { font-size: 50px; font-weight: 700; line-height: 1.1; letter-spacing: -0.5px; white-space: nowrap; }
  .intro-copy { margin-top: 30px; font-size: 18.4px; line-height: 31.2px; font-weight: 400; }

  .app-screen { position: absolute; left: 630px; top: 157px; width: 410px; height: 886px; background: var(--white); border-radius: 40px; overflow: hidden; }

  .map-area { position: absolute; left: 0; top: 100px; width: 410px; height: 652px;
    background: linear-gradient(140deg, var(--map-warm) 0%, var(--map-light) 40%, var(--map-green) 60%, var(--map-light) 75%, #ebebeb 100%); }

  .app-header { position: absolute; left: 0; top: 0; width: 410px; height: 121px; background: var(--brand-red); border-radius: 0 0 37px 37px; color: var(--white); }
  .status-time { position: absolute; left: 37px; top: 16px; font-family: "Arimo", sans-serif; font-weight: 700; font-size: 15px; }
  .status-icons { position: absolute; right: 18px; top: 18px; }
  .app-title { position: absolute; left: 0; right: 0; top: 68px; text-align: center; font-size: 25px; font-weight: 800; }

  .search-bar { position: absolute; left: 31px; top: 140px; width: 351px; height: 49px; background: var(--white); border-radius: 25px; box-shadow: 0 3px 10px rgba(0,0,0,0.12); display: flex; align-items: center; padding: 0 18px 0 26px; }
  .search-bar .placeholder { flex: 1; margin-left: 16px; font-size: 14.5px; color: #6e6e6e; }

  .price-chip { position: absolute; height: 36px; border-radius: 18px; background: var(--brand-red); color: var(--white); font-size: 11px; font-weight: 800; display: flex; align-items: center; justify-content: center; border: 2px solid var(--white); box-shadow: 0 2px 6px rgba(0,0,0,0.15); white-space: nowrap; }
  .chip-mushroom { left: 215px; top: 265px; width: 179px; }
  .chip-tomato { left: 113px; top: 408px; width: 157px; }

  .nearest-card { position: absolute; left: 26px; top: 542px; width: 363px; height: 233px; background: var(--white); border-radius: 28px; overflow: hidden; box-shadow: 0 3px 12px rgba(0,0,0,0.12); }
  .nearest-head { height: 40px; background: var(--cocoa); color: var(--white); display: flex; align-items: center; padding-left: 32px; font-size: 15.5px; font-weight: 600; }
  .nearest-head svg { margin-right: 10px; }
  .nearest-table { width: 313px; margin: 6px auto 0; border-collapse: collapse; table-layout: fixed; font-size: 13.5px; color: var(--ink); }
  .nearest-table td { height: 41px; width: 25%; border-bottom: 1px solid var(--rule); text-align: center; white-space: nowrap; }
  .nearest-table td.name { text-align: left; padding-left: 7px; }

  .tab-bar { position: absolute; left: 0; top: 810px; width: 410px; height: 76px; background: var(--brand-red); border-radius: 37px 37px 0 0; }
  .tab-active { position: absolute; left: 26px; top: 21px; width: 100px; height: 39px; border-radius: 20px; background: var(--white); color: var(--brand-red); display: flex; align-items: center; justify-content: center; gap: 6px; font-size: 15px; font-weight: 700; }
  .tab-icon { position: absolute; top: 29px; }
</style>
</head>
<body>

<section class="intro">
  <h1 class="intro-title">Pebble and Pine</h1>
  <p class="intro-copy">Lorem Ipsum is simply dummy text of the printing and typesetting industry. Lorem Ipsum has been the industry's standard dummy text ever since the 1500s, when an unknown printer took a galley of type and scrambled it to make a type specimen book. It has survived not only five centuries, but also the leap into electronic typesetting, remaining essentially unchanged. It was popularised in the 1960s with the release of Typeline sheets containing Lorem Ipsum passages, and more recently with desktop publishing software like Folio PageSetter including versions of Lorem Ipsum.</p>
</section>

<main class="app-screen">
  <div class="map-area" role="img" aria-label="Street map of the city centre showing nearby cafes and eateries"></div>

  <header class="app-header">
    <span class="status-time">9:41</span>
    <svg class="status-icons" width="70" height="12" viewBox="0 0 70 12">
      <g fill="#fff">
        <rect x="0" y="8" width="3" height="4" rx="1"/><rect x="5" y="6" width="3" height="6" rx="1"/>
        <rect x="10" y="3" width="3" height="9" rx="1"/><rect x="15" y="0" width="3" height="12" rx="1"/>
        <path d="M24 4a10 10 0 0 1 14 0l-1.6 1.6a7.7 7.7 0 0 0-10.8 0z"/>
        <path d="M27 7a5.6 5.6 0 0 1 8 0l-1.6 1.6a3.3 3.3 0 0 0-4.8 0z"/>
        <circle cx="31" cy="10.5" r="1.4"/>
        <rect x="44" y="1" width="22" height="10" rx="2.5" fill="none" stroke="#fff" stroke-width="1"/>
        <rect x="46" y="3" width="18" height="6" rx="1.2"/>
        <rect x="67" y="4" width="1.5" height="4" rx="0.7"/>
      </g>
    </svg>
    <div class="app-title">Pebble and Pine</div>
  </header>

  <div class="search-bar">
    <svg width="18" height="18" viewBox="0 0 18 18"><circle cx="7.5" cy="7.5" r="6" fill="none" stroke="var(--brand-red)" stroke-width="1.8"/><path d="M12 12l5 5" stroke="var(--brand-red)" stroke-width="1.8" stroke-linecap="round"/></svg>
    <span class="placeholder">Seach Soups</span>
    <svg width="20" height="20" viewBox="0 0 20 20" fill="none" stroke="var(--brand-red)" stroke-width="1.3"><rect x="1" y="1" width="18" height="18" rx="3"/><path d="M4 6h12M4 10h12M4 14h12"/><circle cx="7" cy="6" r="1.3" fill="#fff"/><circle cx="13" cy="10" r="1.3" fill="#fff"/><circle cx="8" cy="14" r="1.3" fill="#fff"/></svg>
  </div>

  <div class="price-chip chip-mushroom">$500 - Murshroom Special</div>
  <div class="price-chip chip-tomato">$300 - Tomato Special</div>

  <section class="nearest-card">
    <div class="nearest-head">
      <svg width="18" height="16" viewBox="0 0 18 16" fill="#fff"><path d="M6 1q1 1 0 2t0 2M9 1q1 1 0 2t0 2M12 1q1 1 0 2t0 2" stroke="#fff" stroke-width="0.9" fill="none"/><rect x="0" y="7" width="18" height="2" rx="1"/><path d="M1.5 10h15a7.5 5 0 0 1-15 0z"/></svg>
      Nearest Establishments
    </div>
    <table class="nearest-table">
      <tr><td class="name">Name</td><td>Tomato</td><td>Special</td><td>800m</td></tr>
      <tr><td class="name">Name</td><td>Mushroom</td><td>Special</td><td>300m</td></tr>
      <tr><td class="name">Name</td><td>Sweet Corn</td><td>Special</td><td>500m</td></tr>
      <tr><td class="name">Name</td><td>Sweet Corn</td><td>Special</td><td>500m</td></tr>
    </table>
  </section>

  <nav class="tab-bar">
    <div class="tab-active">
      <svg width="24" height="20" viewBox="0 0 18 16" fill="var(--brand-red)"><path d="M6 1q1 1 0 2t0 2M9 1q1 1 0 2t0 2M12 1q1 1 0 2t0 2" stroke="var(--brand-red)" stroke-width="0.9" fill="none"/><rect x="0" y="7" width="18" height="2" rx="1"/><path d="M1.5 10h15a7.5 5 0 0 1-15 0z"/></svg>
      Soups
    </div>
    <svg class="tab-icon" style="left:161px" width="24" height="24" viewBox="0 0 18 18" fill="#fde3e3"><path d="M6 1q1 1 0 2t0 2M9 1q1 1 0 2t0 2M12 1q1 1 0 2t0 2" stroke="#fde3e3" stroke-width="0.9" fill="none"/><rect x="0" y="7" width="18" height="2.2" rx="1"/><path d="M1.5 10.5h15a7.5 6 0 0 1-15 0z"/></svg>
    <svg class="tab-icon" style="left:260px" width="22" height="24" viewBox="0 0 20 22" fill="#fde3e3"><circle cx="10" cy="6" r="5"/><path d="M0 22v-3a6 6 0 0 1 6-6h8a6 6 0 0 1 6 6v3z"/></svg>
    <svg class="tab-icon" style="left:357px" width="24" height="24" viewBox="0 0 24 24"><circle cx="12" cy="12" r="8" fill="none" stroke="#fde3e3" stroke-width="4" stroke-dasharray="3.2 3.1"/><circle cx="12" cy="12" r="6.5" fill="#fde3e3"/><circle cx="12" cy="12" r="3" fill="var(--brand-red)"/></svg>
  </nav>
</main>

</body>
</html>
```